ALL TEXT GRAPHICS TM May 2025 for Instagram

We are looking for a series of social media graphics for Instagram (new size: 4:5 (1080 x 1350 pixels) ratio that are ALL TEXT. We want the following quotes below on each graphic; one quote per graphic. AND, In very small letters at the bottom of each graphic, add @TovaMarshOnline
The look and feel of these graphics should be complimentary to the color palette attached below; but keep them simple. But the design is up to you; at the end of this document, I provided various samples of all text graphics that I like as examples.
Target Market(s)
women looking to lose weight
Look and feel

```html
<!DOCTYPE html>
<html lang="en">
<head>
<meta charset="utf-8">
<title>Instagram Text Graphics – Tova Marsh</title>
<link rel="stylesheet" href="https://fonts.googleapis.com/css2?family=Inter:wght@300;400;700;800;900&family=Lobster&family=Poppins:wght@700&display=swap">
<style>
  :root {
    --board-green: #1a7a1e;
    --magenta: #d4006a;
    --blush: #fdd4ea;
    --bubblegum: #ff6cb4;
    --hot-pink: #ff0a8a;
    --white: #ffffff;
    --ink: #111111;
  }
  * { margin: 0; padding: 0; box-sizing: border-box; }
  html, body {
    width: 754px; height: 1200px; overflow: hidden;
    background: var(--board-green);
    font-family: "Inter", sans-serif;
  }
  .board { position: relative; width: 754px; height: 1200px; }
  .post { position: absolute; width: 334px; height: 334px; overflow: hidden; }
  .post--deep { background: var(--magenta); color: var(--white); }
  .post--light { background: var(--blush); color: var(--magenta); }
  .col-left { left: 31px; } .col-right { left: 391px; }
  .row-1 { top: 77px; } .row-2 { top: 438px; } .row-3 { top: 790px; }

  .abs { position: absolute; }
  .headline { font-weight: 900; letter-spacing: -0.02em; white-space: nowrap; }
  .body-copy { font-weight: 300; letter-spacing: 0.01em; }
  .centered { left: 0; right: 0; text-align: center; }
  .band { position: absolute; left: 0; right: 0; display: flex; align-items: center; justify-content: center; }
  .handle {
    position: absolute; left: 0; right: 0; top: 308px; text-align: center;
    font-family: "Poppins", sans-serif; font-weight: 700; font-size: 10px; line-height: 12px;
  }
  .post--deep .handle { color: var(--white); }
  .post--light .handle { color: var(--ink); }
  .emph-underline { font-weight: 800; text-decoration: underline; text-decoration-thickness: 2px; text-underline-offset: 2px; }

  /* Post 1 */
  .tired-tag { left: 83px; top: 27px; width: 169px; height: 31px; background: var(--blush); color: var(--magenta);
    font-size: 22px; display: flex; align-items: center; justify-content: center; font-weight: 400; }
  .p1-head { top: 60px; font-size: 56px; line-height: 50px; }
  .p1-body { top: 171px; font-size: 29px; line-height: 31px; }
  .p1-band { top: 251px; height: 45px; background: var(--bubblegum); font-weight: 900; font-size: 40px; letter-spacing: -0.02em; }

  /* Post 2 */
  .p2-that { left: 29px; top: 43px; font-family: "Lobster", cursive; font-size: 38px; line-height: 44px; color: var(--ink); }
  .p2-stubborn { left: 27px; top: 73px; font-size: 60px; line-height: 60px; }
  .p2-weight { left: 26px; top: 131px; font-size: 68px; line-height: 60px; }
  .p2-body { left: 28px; right: 18px; top: 210px; font-size: 23px; line-height: 26px; color: var(--ink); }
  .p2-body strong { font-weight: 900; color: var(--magenta); letter-spacing: -0.01em; }

  /* Post 3 */
  .the-tag { left: 67px; top: 17px; width: 63px; height: 30px; background: var(--hot-pink); color: var(--white);
    transform: rotate(-4deg); font-weight: 700; font-size: 20px; display: flex; align-items: center; justify-content: center; }
  .p3-head { top: 47px; font-size: 56px; line-height: 50px; }
  .p3-body { top: 200px; font-size: 23px; line-height: 24px; color: var(--ink); }
  .p3-band { top: 255px; height: 45px; background: var(--magenta); color: var(--white); font-weight: 900; font-size: 37px; letter-spacing: -0.02em; }

  /* Post 4 */
  .p4-head { left: 24px; top: 41px; font-size: 58px; line-height: 52px; }
  .p4-head .fat { text-decoration: underline; text-decoration-thickness: 4px; text-underline-offset: 4px; }
  .p4-body { left: 25px; right: 12px; top: 169px; font-size: 24px; line-height: 30px; }

  /* Post 5 */
  .p5-head { top: 25px; font-size: 44px; line-height: 43px; }
  .possible-box { left: 19px; top: 118px; width: 296px; height: 48px; background: var(--blush); color: var(--magenta);
    display: flex; align-items: center; justify-content: center; font-weight: 900; font-size: 33px; letter-spacing: -0.02em; }
  .p5-body { left: 25px; right: 10px; top: 189px; font-size: 23px; line-height: 32px; }
  .p5-body strong { font-weight: 800; }

  /* Post 6 */
  .p6-head { left: 22px; top: 16px; font-size: 37px; line-height: 44px; }
  .p6-band { position: absolute; left: 0; right: 0; top: 156px; height: 84px; background: var(--hot-pink); }
  .p6-band-copy { left: 27px; top: 11px; font-size: 24px; line-height: 31px; color: var(--white); }
  .p6-cta { left: 22px; top: 244px; font-size: 37px; line-height: 44px; }
</style>
</head>
<body>
<main class="board">

  <section class="post post--deep col-left row-1">
    <div class="abs tired-tag">Tired. Moody.</div>
    <h2 class="abs headline centered p1-head">Stubborn<br>Belly Fat.</h2>
    <p class="abs body-copy centered p1-body">Your hormones are<br>screaming for help!</p>
    <div class="band p1-band">Let’s fix that.</div>
    <p class="handle">@TovaMarshOnline</p>
  </section>

  <section class="post post--light col-right row-1">
    <span class="abs p2-that">That</span>
    <h2 class="abs headline p2-stubborn">Stubborn</h2>
    <h2 class="abs headline p2-weight">Weight?</h2>
    <p class="abs p2-body">Your hormones are to blame and you’re not alone; <strong>But there is a fix.</strong></p>
    <p class="handle">@TovaMarshOnline</p>
  </section>

  <section class="post post--light col-left row-2">
    <h2 class="abs headline centered p3-head">Stubborn<br>Belly Fat.<br>After 40?</h2>
    <div class="abs the-tag">The</div>
    <p class="abs body-copy centered p3-body" style="font-weight:400">It’s not about calories; it’s<br>about your hormones.</p>
    <div class="band p3-band">Here is the fix!</div>
    <p class="handle">@TovaMarshOnline</p>
  </section>

  <section class="post post--deep col-right row-2">
    <h2 class="abs headline p4-head">Your belly<br>isn’t <span class="fat">fat...</span></h2>
    <p class="abs body-copy p4-body">it’s hormonal. And here’s how to fix it. Comment <span class="emph-underline">HORMONES</span> if nothing is working.</p>
    <p class="handle">@TovaMarshOnline</p>
  </section>

  <section class="post post--deep col-left row-3">
    <h2 class="abs headline centered p5-head">Flat Tummy<br>in Your 40s?</h2>
    <div class="abs possible-box">It’s Still Possible!</div>
    <p class="abs body-copy p5-body">Comment <span class="emph-underline">BYE BELLY</span> to get the 10 secrets to a <strong>flatter tummy</strong></p>
    <p class="handle">@TovaMarshOnline</p>
  </section>

  <section class="post post--light col-right row-3">
    <h2 class="abs headline p6-head">Bloating.<br>Muffin Top.<br>Puffy Waistline</h2>
    <div class="p6-band">
      <p class="abs body-copy p6-band-copy">Your body’s screaming<br>for a different kind of fix.</p>
    </div>
    <p class="abs headline p6-cta">HERE IT IS</p>
    <p class="handle">@TovaMarshOnline</p>
  </section>

</main>
</body>
</html>
```